Business Card Design Project

Bold, modern, clean business card design needed. Prefer double sided with art logo on the back. Front of card with company name logo, no art.

Target Market(s)

Our consulting company supports local, state and federal law enforcement officers. Therefore the design should be clean and direct with no flash or arrogance to it.

Industry/Entity Type

Business

```html
<!DOCTYPE html>
<html lang="en">
<head>
<meta charset="utf-8">
<title>Corvane Systems – Business Cards</title>
<link href="https://fonts.googleapis.com/css2?family=Open+Sans:wght@300;400;700&family=Open+Sans+Condensed:wght@700&display=swap" rel="stylesheet">
<style>
  :root {
    --backdrop: #e7e5e1;
    --card: #ffffff;
    --card-shade: #ececec;
    --ink: #3a3a3a;
    --ink-soft: #6b6b6b;
    --accent: #a6cc4a;
    --band: #111111;
  }
  * { margin: 0; padding: 0; box-sizing: border-box; }
  html, body {
    width: 1200px; height: 1023px; overflow: hidden;
    background: var(--backdrop);
    font-family: "Open Sans", Arial, sans-serif;
  }
  .stage { position: relative; width: 1200px; height: 1023px; }

  .card {
    position: absolute;
    width: 560px; height: 320px;
    background: var(--card);
    border-radius: 4px;
    overflow: hidden;
    box-shadow: 0 8px 22px rgba(0,0,0,.18);
  }

  /* Front */
  .card-front { left: 80px; top: 140px; }
  .front-corner-mark {
    position: absolute; right: -70px; top: -110px;
    width: 230px; height: 230px; border-radius: 50%;
    background: var(--band);
  }
  .front-wordmark {
    position: absolute; left: 36px; top: 44px;
    font-weight: 300; font-size: 40px; letter-spacing: .5px;
    color: var(--ink); white-space: nowrap;
  }
  .person { position: absolute; left: 38px; top: 128px; }
  .person-name {
    font-weight: 700; font-size: 19px; color: var(--accent); letter-spacing: .3px;
  }
  .person-role {
    font-size: 11px; color: var(--ink-soft); text-transform: uppercase; margin-top: 2px;
  }
  .contact-list { list-style: none; margin-top: 12px; }
  .contact-list li {
    display: flex; align-items: center; gap: 10px;
    font-size: 13px; color: var(--ink); line-height: 22px;
  }
  .contact-icon {
    width: 14px; height: 14px; border-radius: 2px;
    background: var(--accent);
    display: inline-flex; align-items: center; justify-content: center;
  }
  .address-band {
    position: absolute; left: 0; right: 0; bottom: 0; height: 40px;
    background: var(--band);
    display: flex; align-items: center; padding-left: 38px;
    font-family: "Open Sans Condensed", "Arial Narrow", sans-serif;
    font-weight: 700; font-size: 15px; color: var(--accent);
    text-transform: uppercase; letter-spacing: .4px;
  }

  /* Back */
  .card-back {
    left: 580px; top: 580px;
    background: radial-gradient(ellipse at center, var(--card) 40%, var(--card-shade) 100%);
    display: flex; align-items: center; justify-content: center; gap: 16px;
  }
  .back-circle {
    width: 44px; height: 44px; border-radius: 50%; background: var(--accent);
  }
  .back-wordmark {
    font-weight: 300; font-size: 38px; color: var(--ink); letter-spacing: 1px;
  }
</style>
</head>
<body>
<main class="stage">

  <section class="card card-front" aria-label="Business card front">
    <div class="front-corner-mark"></div>
    <div class="front-wordmark">Corvane Systems</div>

    <div class="person">
      <div class="person-name">DANIEL R. MARSH</div>
      <div class="person-role">Manager</div>
      <ul class="contact-list">
        <li>
          <span class="contact-icon">
            <svg width="9" height="9" viewBox="0 0 10 10"><path d="M2 1h2l1 2-1.2 1a6 6 0 0 0 2.2 2.2L7 5l2 1v2c0 .6-.4 1-1 1A8 8 0 0 1 1 2c0-.6.4-1 1-1z" fill="#fff"/></svg>
          </span>555-014-2287
        </li>
        <li>
          <span class="contact-icon">
            <svg width="9" height="9" viewBox="0 0 10 10"><rect x="1" y="2.5" width="8" height="5.5" fill="none" stroke="#fff" stroke-width="1"/><path d="M1 2.5l4 3 4-3" fill="none" stroke="#fff" stroke-width="1"/></svg>
          </span>daniel@corvanesystems.com
        </li>
        <li>
          <span class="contact-icon">
            <svg width="9" height="9" viewBox="0 0 10 10"><circle cx="5" cy="5" r="3.8" fill="none" stroke="#fff" stroke-width="1"/><path d="M1.2 5h7.6M5 1.2c-2 2.5-2 5.1 0 7.6M5 1.2c2 2.5 2 5.1 0 7.6" fill="none" stroke="#fff" stroke-width=".8"/></svg>
          </span>www.corvanesystems.com
        </li>
      </ul>
    </div>

    <div class="address-band">2250 Hollis Ave, Suite C4 Brookfield MD 20911</div>
  </section>

  <section class="card card-back" aria-label="Business card back">
    <div class="back-circle"></div>
    <div class="back-wordmark">Corvane Systems</div>
  </section>

</main>
</body>
</html>
```